ALL TYPES OF COMMERCIAL PLASTERING

TYPE OF BLOCK LETTERING WITH STAND OUT QUALITIES
WITH SOME TYPE OF LOGO
SOMETHING UNIQUE FOR THE BUILDING INDUSTRY.
QUALITY WORKMANSHIP
Updates

forgot to include my mobile phone number on my brief. could you add it to your design please MOBILE PH 0412 858 196

please let me make this quite clear ,the company name is harbourline linings and Fitouts PTY LTD. THE TYPE OF WORK WE WILL BE DOING IS COMMERCIAL PLASTERING.

Industry/Entity Type

Industry

Contact Information for Business Card

harbourline linings and fitouts P/L
marcus devlin p.o.box 42 wendouree 3355 email address harbourlinelinings@examplemail.com
ABN 51 718 294 605 COMMERCIAL PLASTERING

```html
<!DOCTYPE html>
<html lang="en">
<head>
<meta charset="utf-8">
<title>Harbourline Linings and Fitouts – Business Card</title>
<link rel="stylesheet" href="https://fonts.googleapis.com/css2?family=Orbitron:wght@600&family=Lato:wght@700;900&display=swap">
<style>
  :root {
    --page: #e9e5df;
    --rust: #b4571f;
    --rust-dark: #9c4716;
    --plaster-top: #efd2a6;
    --plaster-mid: #f4efe6;
    --plaster-white: #f7f5f0;
    --brick: #c2622a;
    --brick-dark: #9a4a22;
    --strip: #efdcc0;
  }
  * { margin: 0; padding: 0; box-sizing: border-box; }
  html, body {
    width: 1200px;
    height: 900px;
    overflow: hidden;
    background: var(--page);
  }
  .canvas {
    position: relative;
    width: 1200px;
    height: 900px;
    display: flex;
    align-items: center;
    justify-content: center;
  }
  .business-card {
    position: relative;
    width: 980px;
    height: 560px;
    overflow: hidden;
    box-shadow: 0 12px 34px rgba(0,0,0,0.18);
  }
  .wall-texture {
    position: absolute;
    inset: 0;
    background: linear-gradient(180deg,
      var(--plaster-top) 0%,
      #f1dcbc 30%,
      var(--plaster-mid) 48%,
      var(--plaster-white) 60%,
      var(--brick) 68%,
      #b85a28 78%,
      var(--brick-dark) 86%,
      var(--strip) 88%,
      var(--strip) 100%);
  }
  .company-name {
    position: absolute;
    left: 50px;
    top: 58px;
    font-family: "Orbitron", sans-serif;
    font-weight: 600;
    font-size: 34px;
    letter-spacing: 2px;
    color: var(--rust);
    white-space: nowrap;
  }
  .trade {
    position: absolute;
    left: 196px;
    top: 110px;
    font-family: "Lato", sans-serif;
    font-weight: 700;
    font-size: 24px;
    letter-spacing: 7px;
    color: var(--rust-dark);
    white-space: nowrap;
  }
  .person-name {
    position: absolute;
    left: 58px;
    top: 196px;
    font-family: "Lato", sans-serif;
    font-weight: 900;
    font-size: 34px;
    letter-spacing: 1px;
    color: var(--rust);
    white-space: nowrap;
  }
  .contact-list {
    position: absolute;
    left: 490px;
    top: 164px;
    list-style: none;
    font-family: "Lato", sans-serif;
    font-weight: 700;
    font-size: 18px;
    line-height: 28px;
    color: var(--rust);
    white-space: nowrap;
  }
  .tagline {
    position: absolute;
    left: 0;
    right: 0;
    bottom: 14px;
    text-align: center;
    font-family: "Lato", sans-serif;
    font-weight: 900;
    font-size: 28px;
    letter-spacing: 16px;
    color: var(--rust);
    white-space: nowrap;
  }
</style>
</head>
<body>
  <main class="canvas">
    <article class="business-card">
      <div class="wall-texture" role="img" aria-label="Photograph of a weathered plaster wall peeling away to reveal orange brickwork"></div>
      <h1 class="company-name">HARBOURLINE LININGS AND FITOUTS</h1>
      <p class="trade">COMMERCIAL PLASTERING</p>
      <p class="person-name">MARCUS DEVLIN</p>
      <ul class="contact-list">
        <li>Email: harbourlinelinings@examplemail.com</li>
        <li>P.O.Box 42 Wendouree 3355</li>
        <li>ABN 51 718 294 605</li>
      </ul>
      <p class="tagline">QUALITY WORKMANSHIP</p>
    </article>
  </main>
</body>
</html>
```